K&R Security Services PTY. LTD.

Ive just had my logo made and I'm looking for some simple but strong designs for my business cards the company is a security company.

Please use dark colors.

Regards,

Owen Deloit

Reason: Need more time for discussion with other directors

Industry/Entity Type

Security

Font styles to use
Sans Serif
Decorative

```html
<!DOCTYPE html>
<html lang="en">
<head>
<meta charset="utf-8">
<title>K&amp;R Security Services – Business Cards</title>
<link rel="stylesheet" href="https://fonts.googleapis.com/css2?family=PT+Serif:wght@400;700&display=swap">
<style>
  :root {
    --page: #d9d9da;
    --charcoal: #37373a;
    --charcoal-deep: #2b2b2e;
    --steel: #8d8d90;
    --steel-light: #a9a9ac;
    --silver-line: #c4c4c7;
    --ink-light: #f1f1f2;
    --ink-dark: #2e2e31;
  }
  * { box-sizing: border-box; margin: 0; padding: 0; }
  html, body {
    width: 1200px; height: 1200px; overflow: hidden;
    background: var(--page);
    font-family: "PT Serif", Georgia, serif;
  }
  .sheet {
    width: 1200px; height: 1200px;
    display: flex; flex-direction: column; align-items: center; justify-content: center;
    gap: 40px;
  }
  .card {
    position: relative;
    width: 900px; height: 514px;
    overflow: hidden;
    box-shadow: 0 10px 28px rgba(0,0,0,0.22);
  }
  .card-bg { position: absolute; inset: 0; width: 100%; height: 100%; }

  .brand {
    position: absolute;
    display: flex; align-items: center; gap: 14px;
    color: var(--ink-light);
    font-weight: 700;
    letter-spacing: 0.04em;
  }
  .brand-mark {
    width: 22px; height: 22px; border-radius: 50%;
    background: var(--ink-light);
    flex: none;
  }
  .card-front .brand {
    left: 0; right: 0; top: 150px; justify-content: center;
    font-size: 30px;
  }
  .card-back .brand {
    right: 48px; top: 215px;
    font-size: 18px;
    max-width: 300px; line-height: 1.35;
  }

  .holder { position: absolute; left: 60px; top: 64px; color: var(--ink-light); }
  .holder-name { font-size: 44px; font-weight: 400; letter-spacing: 0.01em; }
  .holder-title {
    margin-top: 6px; font-size: 15px; text-transform: uppercase; letter-spacing: 0.14em;
    color: var(--silver-line);
  }

  .contact {
    position: absolute; left: 60px; top: 250px;
    font-size: 18px; line-height: 1.6; color: var(--ink-dark);
  }
  .contact-row { display: flex; gap: 10px; }
  .contact-label { min-width: 132px; }
</style>
</head>
<body>
<main class="sheet">

  <section class="card card-front" aria-label="Business card front">
    <svg class="card-bg" viewBox="0 0 900 514" preserveAspectRatio="none" aria-hidden="true">
      <rect width="900" height="514" fill="var(--charcoal)"/>
      <path d="M0 300 C 260 250, 560 330, 900 420 L900 514 L0 514 Z" fill="var(--steel)"/>
      <path d="M0 300 C 260 250, 560 330, 900 420" fill="none" stroke="var(--silver-line)" stroke-width="3"/>
      <path d="M0 430 C 300 400, 600 470, 900 500 L900 514 L0 514 Z" fill="var(--charcoal-deep)"/>
    </svg>
    <div class="brand"><span class="brand-mark"></span>K&amp;R Security Services PTY. LTD.</div>
  </section>

  <section class="card card-back" aria-label="Business card back">
    <svg class="card-bg" viewBox="0 0 900 514" preserveAspectRatio="none" aria-hidden="true">
      <rect width="900" height="514" fill="var(--steel-light)"/>
      <path d="M0 0 L900 0 L900 514 C 800 330, 560 200, 0 180 Z" fill="var(--charcoal)"/>
      <path d="M0 180 C 560 200, 800 330, 900 514" fill="none" stroke="var(--silver-line)" stroke-width="4"/>
      <path d="M0 470 C 300 430, 650 470, 900 514 L0 514 Z" fill="var(--steel)"/>
    </svg>
    <div class="holder">
      <h1 class="holder-name">Owen Deloit</h1>
      <p class="holder-title">Security Director</p>
    </div>
    <div class="brand"><span class="brand-mark"></span>K&amp;R Security Services PTY. LTD.</div>
    <div class="contact">
      <p>P.O. Box 7 | Elmwood Victoria 3081</p>
      <p class="contact-row"><span class="contact-label">Mobile:</span>0400 555 183</p>
      <p class="contact-row"><span class="contact-label">Phone:</span>(03) 9555 0147</p>
      <p class="contact-row"><span class="contact-label">Email:</span>owen@deloit-mail.net.au</p>
      <p class="contact-row"><span class="contact-label">Business e-mail:</span>office@kr-guard.net.au</p>
    </div>
  </section>

</main>
</body>
</html>
```